Medical IT Business with New logo needs a fresh stationary design

First time on sketch Harbor; Thought I would give it a go.
This project is for business cards alone but we have loads of design work that needs to take place in the immediate future.

We provide IT services to the Medical Industry and value ourselves as offering a premium product to the market.

I am after a fresh, clean design using full colour 2 sided cards which includes our current colour palettes from our logo.

Card's must include:
- Logo
- Slogan
- Name
- Adress
- Email
- Phone
- Fax
- Mobile

Target Market(s)

Surgeons, High Profile Medical Personnel

Industry/Entity Type

Business

Fonts, CMYK Colours and Logo files attached.

Requirements
Must have
• Card's must include:
• - Logo
• - Slogan
• - Name
• - Adress
• - Email
• - Phone
• - Fax
• - Mobile
Nice to have
• Needs to incorporate our colour palette (attached CMYK colours)
Should not have
• Black backgrounds. Black text ok.

```html
<!DOCTYPE html>
<html lang="en">
<head>
<meta charset="utf-8">
<title>Caretrail Systems – Business Card</title>
<link href="https://fonts.googleapis.com/css2?family=Source+Sans+3:wght@400;600;700&display=swap" rel="stylesheet">
<style>
  :root {
    --backdrop: #e6e7e9;
    --card-light: #f4f4f5;
    --navy: #0d2d5e;
    --brand-blue: #1b7cb9;
    --text-grey: #4a4d52;
    --slogan-grey: #8797ab;
    --slogan-light: #8fb8dc;
    --url-light: #c9d3e3;
    --white: #ffffff;
  }
  * { margin: 0; padding: 0; box-sizing: border-box; }
  html, body {
    width: 1105px; height: 1200px; overflow: hidden;
    background: var(--backdrop);
    font-family: "Source Sans 3", "Myriad Pro", sans-serif;
  }
  .card {
    position: absolute; left: 182px; width: 746px; height: 425px; overflow: hidden;
  }
  .card--front { top: 119px; background: var(--card-light); }
  .card--back { top: 637px; background: var(--navy); }

  .front__band {
    position: absolute; left: 0; top: 54px; width: 113px; height: 104px;
    background: var(--navy);
  }
  .brand-dot {
    position: absolute; border-radius: 50%;
    background: var(--brand-blue); border: 3px solid var(--white);
  }
  .front .brand-dot { left: 61px; top: 53px; width: 104px; height: 104px; }
  .brand-name {
    position: absolute; font-weight: 700; line-height: 0.98; text-transform: uppercase;
  }
  .brand-name span { display: block; }
  .brand-name .brand-name__second { letter-spacing: 0.09em; }
  .front .brand-name { left: 178px; top: 58px; font-size: 37px; color: var(--navy); }
  .slogan { position: absolute; font-weight: 400; white-space: nowrap; }
  .front .slogan { left: 180px; top: 128px; font-size: 16px; color: var(--slogan-grey); }

  .address {
    position: absolute; left: 178px; top: 187px;
    font-size: 19px; line-height: 28px; color: var(--text-grey);
  }
  .contacts {
    position: absolute; left: 178px; top: 247px; list-style: none;
    font-size: 19px; line-height: 28.5px; color: var(--text-grey);
  }
  .contacts li { display: flex; align-items: center; gap: 9px; }
  .contacts svg { width: 17px; height: 17px; fill: var(--navy); flex: none; }

  .person { position: absolute; right: 51px; top: 253px; text-align: right; }
  .person__name { font-size: 26px; font-weight: 600; color: var(--navy); line-height: 1.1; }
  .person__role { font-size: 20px; color: var(--brand-blue); line-height: 1.3; }

  .back .brand-dot { left: 166px; top: 152px; width: 124px; height: 124px; border: none; }
  .back .brand-name { left: 304px; top: 158px; font-size: 43px; color: var(--white); }
  .back .slogan { left: 306px; top: 240px; font-size: 19px; color: var(--slogan-light); }
  .back__url {
    position: absolute; left: 0; right: 0; top: 355px; text-align: center;
    font-size: 20px; letter-spacing: 0.32em; color: var(--url-light);
  }
</style>
</head>
<body>
  <section class="card card--front front">
    <div class="front__band"></div>
    <div class="brand-dot"></div>
    <div class="brand-name"><span>Caretrail</span><span class="brand-name__second">Systems</span></div>
    <p class="slogan">connected to your clinic</p>

    <p class="address">1420 Willowmere Court<br>Juneau, Alaska 99801</p>

    <ul class="contacts">
      <li><svg viewBox="0 0 16 16"><path d="M3.6 1l2.6 3-1.4 1.8c.9 1.9 2.5 3.5 4.4 4.4L11 8.8l3 2.6-1.3 2.9C7 14 2 9 1.7 3.3z"/></svg>555 210 4471</li>
      <li><svg viewBox="0 0 16 16"><path d="M4 1h8v14H4zM5.5 2.5v9.5h5V2.5zM7.2 13h1.6v1H7.2z"/></svg>555 318 2096</li>
      <li><svg viewBox="0 0 16 16"><path d="M4 1h7l1 1v4H4zM1 7h14v6h-2v-2H3v2H1zM4 12h8v3H4z"/></svg>555 762 0385</li>
      <li><svg viewBox="0 0 16 16"><path d="M1 4h14v9H1zM2.3 5.2L8 9.2l5.7-4H2.3z"/></svg>daniel@caretrail.com</li>
      <li><svg viewBox="0 0 16 16"><path d="M8 1a7 7 0 1 0 0 14A7 7 0 0 0 8 1zm-1 2.2c-.3.8.4 1.6 1.3 1.5.8 0 1 1 .3 1.5-.9.5-2 .2-2.6 1-.5.8.5 1.8 1.4 1.9.8.1 1 1.2.6 1.9l-.7 1.8A5.2 5.2 0 0 1 7 3.2zm4 .9a5.2 5.2 0 0 1 .8 7.4c-.4-.8-1.3-1.1-1.4-2-.1-1 1-1.4.7-2.3-.3-.8-1.6-.6-1.6-1.5 0-.8 1.2-1 1.5-1.6z"/></svg>www.caretrail.com</li>
    </ul>

    <div class="person">
      <p class="person__name">Daniel Reyes</p>
      <p class="person__role">CEO/Founder</p>
    </div>
  </section>

  <section class="card card--back back">
    <div class="brand-dot"></div>
    <div class="brand-name"><span>Caretrail</span><span class="brand-name__second">Systems</span></div>
    <p class="slogan">connected to your clinic</p>
    <p class="back__url">www.caretrail.com</p>
  </section>
</body>
</html>
```